IT Tradingsystem for car dealers needs Business Card Design

We need a fresh and modern design for our new business cards.

We develop a it-business system for car dealers in Sweden, Norway and on our way down to further countries in Europe, hence the namechange to BrolaTek Europe AB. The site can be found at www.brolatek-example.com. The startpage is also in for an update/modernization soon so don't take to much from here.

We are looking to print double sided, 4-colour cards.

We want to look professional, modern and serious. Open to cooler suggestions, but not too crazy. We need to make a good and serious impression on our potential customers. It needs to reflect our scandinavian design values and layout.

Preferably with the full BrolaTek logo in good size on the back, so the small print on the logo can be read easily.

Text that needs to go on the cards:
-------

Per Oskar Fjellström
Founder

Direct +46 70-512 96 47
Support 08-612 57 394
po.fjellstrom@brolatek-example.com

BrolaTek Europe AB
Box 8617
104 29 Stockholm

Brolatek-example.com
Saljportalen-example.se

--------
Good luck and thanks!

PS. If you need more input or see what our previous cards looked like, don't hesitate to contact me!

Target Market(s)

Decision makers / executives at brand cardealers

Industry/Entity Type

Automotive

Contact Information for Business Card

Normal size

Requirements
Must have
• Full logo
Nice to have
• Base on our orange colors
Should not have
• No fonts with serif, and not too much graphics

```html
<!DOCTYPE html>
<html lang="en">
<head>
<meta charset="utf-8">
<title>BrolaTek Business Card</title>
<link href="https://fonts.googleapis.com/css2?family=Lato:wght@400;700&family=Montserrat:wght@700;800&display=swap" rel="stylesheet">
<style>
  :root{
    --bg:#1c1c1e;
    --card:#0d0d0d;
    --gold:#e6d08a;
    --gold-light:#f6e7a8;
    --gold-dark:#a8873e;
    --olive:#3a392d;
    --text-gold:#d9c58a;
  }
  *{margin:0;padding:0;box-sizing:border-box}
  html,body{width:1200px;height:800px;overflow:hidden;background:var(--bg)}
  .canvas{position:relative;width:1200px;height:800px}
  .card{position:absolute;width:540px;height:309px;background:var(--card);overflow:hidden;box-shadow:0 18px 40px rgba(0,0,0,.55)}
  .card--back{left:40px;top:245px}
  .card--front{left:620px;top:245px;background:linear-gradient(160deg,#1b1b1b 0%,#0b0b0b 55%,#121212 100%)}

  /* back side */
  .pattern-field{position:absolute;inset:0;background:linear-gradient(135deg,#6b5426 0%,#c9ac62 35%,#8a6d34 60%,#d8bf7a 100%)}
  .logo-oval{position:absolute;left:70px;top:92px;width:400px;height:125px;border-radius:50%;background:radial-gradient(ellipse at center,#161616 0%,#050505 100%);display:flex;flex-direction:column;align-items:center;justify-content:center}
  .logo-row{display:flex;align-items:center;gap:12px}
  .logo-square{width:30px;height:30px;background:var(--gold)}
  .logo-name{font-family:"Montserrat",sans-serif;font-weight:800;font-size:38px;color:var(--gold);letter-spacing:.5px}
  .logo-tagline{font-family:"Lato",sans-serif;font-size:10px;color:var(--text-gold);letter-spacing:1px;margin-top:4px;margin-left:42px}

  /* front side */
  .front-art{position:absolute;inset:0}
  .holder{position:absolute;left:0;right:0;top:58px;text-align:center}
  .holder-name{font-family:"Montserrat",sans-serif;font-weight:800;font-size:24px;color:var(--gold-light)}
  .holder-title{font-family:"Lato",sans-serif;font-weight:700;font-size:11px;letter-spacing:2px;color:var(--text-gold);margin-top:2px}
  .chevron{display:block;margin:6px auto 0}
  .contacts{position:absolute;top:130px;left:0;right:0;display:flex;justify-content:center}
  .contact-col{display:flex;flex-direction:column;gap:12px;width:255px}
  .contact-col--left{align-items:flex-end;padding-right:14px}
  .contact-col--right{align-items:flex-start;padding-left:14px;border-left:1px solid rgba(217,197,138,.35)}
  .contact{display:flex;align-items:center;gap:10px;font-family:"Lato",sans-serif;font-size:13px;color:var(--text-gold)}
  .contact-col--left .contact{flex-direction:row-reverse}
  .icon{width:26px;height:26px;flex:none}
  .pin{position:absolute;left:259px;top:210px;width:22px;height:22px}
  .address-band{position:absolute;left:0;right:0;top:236px;height:38px;background:var(--olive);display:flex;align-items:center;justify-content:center;font-family:"Lato",sans-serif;font-size:17px;color:var(--text-gold);letter-spacing:.3px}
</style>
</head>
<body>
<div class="canvas">

  <section class="card card--back">
    <div class="pattern-field" role="img" aria-label="Gold and black geometric triangle pattern covering the card"></div>
    <div class="logo-oval">
      <div class="logo-row">
        <span class="logo-square"></span>
        <span class="logo-name">BrolaTek</span>
      </div>
      <div class="logo-tagline">ProvKoll | Remarketing | saljportalen-example.se</div>
    </div>
  </section>

  <section class="card card--front">
    <svg class="front-art" viewBox="0 0 540 309" aria-hidden="true">
      <defs>
        <linearGradient id="goldSweep" x1="0" y1="0" x2="1" y2="0">
          <stop offset="0" stop-color="#8f7234"/>
          <stop offset=".45" stop-color="#f3e29c"/>
          <stop offset="1" stop-color="#a8873e"/>
        </linearGradient>
      </defs>
      <path d="M0 0 H540 V6 C380 12 170 26 0 42 Z" fill="url(#goldSweep)"/>
      <path d="M0 46 C170 30 380 16 540 10 V13 C380 19 170 33 0 49 Z" fill="#6d5a2c"/>
      <path d="M0 309 V276 C160 284 380 292 540 300 V309 Z" fill="url(#goldSweep)"/>
    </svg>

    <div class="holder">
      <div class="holder-name">Per Oskar Fjellström</div>
      <div class="holder-title">FOUNDER</div>
      <svg class="chevron" width="10" height="6" viewBox="0 0 10 6" aria-hidden="true"><path d="M1 1 L5 5 L9 1" fill="none" stroke="#d9c58a" stroke-width="1.2"/></svg>
    </div>

    <div class="contacts">
      <div class="contact-col contact-col--left">
        <div class="contact">
          <svg class="icon" viewBox="0 0 26 26" aria-hidden="true"><circle cx="13" cy="13" r="12" fill="none" stroke="#d9c58a" stroke-width="1.3"/><path d="M9 8 C8 12 12 17 17 18 L18.5 16 L16 14.5 L14.8 15.6 C13 14.6 11.8 13.3 11 11.6 L12.2 10.4 L10.8 7.8 Z" fill="#d9c58a"/></svg>
          <span>08-612 57 394</span>
        </div>
        <div class="contact">
          <svg class="icon" viewBox="0 0 26 26" aria-hidden="true"><circle cx="13" cy="13" r="12" fill="none" stroke="#d9c58a" stroke-width="1.3"/><rect x="7.5" y="9" width="11" height="8" fill="none" stroke="#d9c58a" stroke-width="1.2"/><path d="M7.5 9 L13 13.5 L18.5 9" fill="none" stroke="#d9c58a" stroke-width="1.2"/></svg>
          <span>po.fjellstrom@brolatek-example.com</span>
        </div>
      </div>
      <div class="contact-col contact-col--right">
        <div class="contact">
          <svg class="icon" viewBox="0 0 26 26" aria-hidden="true"><circle cx="13" cy="13" r="12" fill="none" stroke="#d9c58a" stroke-width="1.3"/><rect x="9.5" y="7" width="7" height="12" rx="1.2" fill="none" stroke="#d9c58a" stroke-width="1.2"/><circle cx="13" cy="17" r=".8" fill="#d9c58a"/></svg>
          <span>+46 70-512 96 47</span>
        </div>
        <div class="contact">
          <svg class="icon" viewBox="0 0 26 26" aria-hidden="true"><circle cx="13" cy="13" r="12" fill="none" stroke="#d9c58a" stroke-width="1.3"/><circle cx="13" cy="13" r="6" fill="none" stroke="#d9c58a" stroke-width="1.2"/><path d="M7 13 H19 M13 7 C10 10 10 16 13 19 M13 7 C16 10 16 16 13 19" fill="none" stroke="#d9c58a" stroke-width="1"/></svg>
          <span>www.brolatek-example.com</span>
        </div>
      </div>
    </div>

    <svg class="pin" viewBox="0 0 22 22" aria-hidden="true"><circle cx="11" cy="11" r="11" fill="#e6d08a"/><path d="M11 5 C8.5 5 7 6.8 7 8.8 C7 11.6 11 16 11 16 C11 16 15 11.6 15 8.8 C15 6.8 13.5 5 11 5 Z" fill="#111"/><circle cx="11" cy="8.8" r="1.5" fill="#e6d08a"/></svg>

    <div class="address-band">BrolaTek Europe AB Box 8617 104 29 Stockholm</div>
  </section>

</div>
</body>
</html>
```